KORBALT

The business want a professional looking business card. We have a scetch we will add but want the extra upgrade, and would like more suggestions for variations of our business cards.

```html
<!DOCTYPE html>
<html lang="en">
<head>
<meta charset="UTF-8">
<title>KORBALT – Business Card</title>
<link rel="stylesheet" href="https://fonts.googleapis.com/css2?family=Playfair+Display:wght@700&family=Cinzel:wght@500&family=Poppins:wght@400;500&display=swap">
<style>
  :root {
    --page-bg: #ffffff;
    --card-black: #050505;
    --pattern-tone: #121212;
    --gold: #d9b65a;
    --gold-light: #f1dc8e;
    --gold-deep: #a8832f;
    --shadow: rgba(0, 0, 0, 0.35);
  }
  * { margin: 0; padding: 0; box-sizing: border-box; }
  html, body {
    width: 1200px;
    height: 2211px;
    overflow: hidden;
    background: var(--page-bg);
  }
  .sheet {
    position: relative;
    width: 1200px;
    height: 2211px;
  }
  .card {
    position: absolute;
    left: 180px;
    width: 840px;
    height: 479px;
    background: var(--card-black);
    box-shadow: 18px 26px 34px var(--shadow);
    overflow: hidden;
  }
  .card--front { top: 576px; }
  .card--back  { top: 1155px; }

  .card__pattern {
    position: absolute;
    inset: 0;
    background: radial-gradient(ellipse at center, var(--pattern-tone) 0%, var(--card-black) 75%);
  }
  .card__frame {
    position: absolute;
    inset: 8px;
    border: 2px solid var(--gold);
  }
  .card__ornament {
    position: absolute;
    width: 92px;
    height: 92px;
  }
  .card__ornament--tl { top: 8px; left: 8px;
    background: radial-gradient(circle at 0 0, rgba(217,182,90,0.75) 0%, rgba(217,182,90,0.15) 55%, transparent 72%); }
  .card__ornament--tr { top: 8px; right: 8px;
    background: radial-gradient(circle at 100% 0, rgba(217,182,90,0.75) 0%, rgba(217,182,90,0.15) 55%, transparent 72%); }
  .card__ornament--bl { bottom: 8px; left: 8px;
    background: radial-gradient(circle at 0 100%, rgba(217,182,90,0.75) 0%, rgba(217,182,90,0.15) 55%, transparent 72%); }
  .card__ornament--br { bottom: 8px; right: 8px;
    background: radial-gradient(circle at 100% 100%, rgba(217,182,90,0.75) 0%, rgba(217,182,90,0.15) 55%, transparent 72%); }

  /* Front */
  .brand {
    position: absolute;
    left: 0; right: 0;
    top: 118px;
    text-align: center;
  }
  .brand__dot {
    display: block;
    width: 96px;
    height: 96px;
    margin: 0 auto 36px;
    border-radius: 50%;
    background: var(--gold);
  }
  .brand__name {
    font-family: "Cinzel", serif;
    font-weight: 500;
    font-size: 46px;
    letter-spacing: 10px;
    color: var(--gold);
    line-height: 1;
    padding-left: 10px;
  }
  .brand__since {
    margin-top: 18px;
    font-family: "Poppins", sans-serif;
    font-weight: 500;
    font-size: 15px;
    letter-spacing: 7px;
    color: var(--gold);
    padding-left: 7px;
  }

  /* Back */
  .contact {
    position: absolute;
    left: 0; right: 0;
    top: 80px;
    text-align: center;
    color: var(--gold);
  }
  .contact__name {
    font-family: "Playfair Display", serif;
    font-weight: 700;
    font-size: 44px;
    line-height: 1.1;
    color: var(--gold-light);
  }
  .contact__role {
    margin-top: 4px;
    font-family: "Poppins", sans-serif;
    font-weight: 400;
    font-size: 26px;
    color: var(--gold);
  }
  .contact__rule {
    width: 66px;
    height: 2px;
    margin: 30px auto 28px;
    background: var(--gold);
  }
  .contact__icons {
    display: flex;
    justify-content: center;
    gap: 14px;
  }
  .contact__icons svg { width: 20px; height: 20px; fill: var(--gold); }
  .contact__list {
    margin-top: 22px;
    list-style: none;
    font-family: "Poppins", sans-serif;
    font-weight: 400;
    font-size: 24px;
    line-height: 35px;
  }
</style>
</head>
<body>
<main class="sheet">

  <section class="card card--front" aria-label="Business card front">
    <div class="card__pattern" role="img" aria-label="Faint dark repeating floral knot pattern"></div>
    <div class="card__frame"></div>
    <div class="card__ornament card__ornament--tl" role="img" aria-label="Gold floral corner ornament"></div>
    <div class="card__ornament card__ornament--tr" role="img" aria-label="Gold floral corner ornament"></div>
    <div class="card__ornament card__ornament--bl" role="img" aria-label="Gold floral corner ornament"></div>
    <div class="card__ornament card__ornament--br" role="img" aria-label="Gold floral corner ornament"></div>
    <div class="brand">
      <span class="brand__dot"></span>
      <p class="brand__name">KORBALT</p>
      <p class="brand__since">SINCE 2026</p>
    </div>
  </section>

  <section class="card card--back" aria-label="Business card back">
    <div class="card__pattern" role="img" aria-label="Faint dark repeating floral knot pattern"></div>
    <div class="card__frame"></div>
    <div class="card__ornament card__ornament--tl" role="img" aria-label="Gold floral corner ornament"></div>
    <div class="card__ornament card__ornament--tr" role="img" aria-label="Gold floral corner ornament"></div>
    <div class="card__ornament card__ornament--bl" role="img" aria-label="Gold floral corner ornament"></div>
    <div class="card__ornament card__ornament--br" role="img" aria-label="Gold floral corner ornament"></div>
    <div class="contact">
      <h1 class="contact__name">Lars Henrik Solvang</h1>
      <p class="contact__role">CEO &amp; Founder</p>
      <div class="contact__rule"></div>
      <div class="contact__icons">
        <svg viewBox="0 0 24 24" aria-label="Phone"><path d="M6.6 10.8a15.1 15.1 0 0 0 6.6 6.6l2.2-2.2a1 1 0 0 1 1-.25 11.4 11.4 0 0 0 3.6.57 1 1 0 0 1 1 1V20a1 1 0 0 1-1 1A17 17 0 0 1 3 4a1 1 0 0 1 1-1h3.5a1 1 0 0 1 1 1c0 1.25.2 2.45.57 3.57a1 1 0 0 1-.25 1z"/></svg>
        <svg viewBox="0 0 24 24" aria-label="Email"><path d="M2 5h20v14H2z" fill="none"/><path d="M2 5h20v14H2V5zm2 2v.4l8 5.2 8-5.2V7H4zm16 2.8-8 5.2-8-5.2V17h16V9.8z"/></svg>
        <svg viewBox="0 0 24 24" aria-label="Website"><path d="M12 2a10 10 0 1 0 0 20 10 10 0 0 0 0-20zm6.9 6h-2.9a15.7 15.7 0 0 0-1.4-3.6A8 8 0 0 1 18.9 8zM12 4c.8 1.2 1.5 2.5 1.9 4h-3.8c.4-1.5 1.1-2.8 1.9-4zM4.3 14a8 8 0 0 1 0-4h3.4a16.5 16.5 0 0 0 0 4H4.3zm.8 2h2.9c.3 1.3.8 2.5 1.4 3.6A8 8 0 0 1 5.1 16zM8 8H5.1a8 8 0 0 1 4.3-3.6C8.8 5.5 8.3 6.7 8 8zm4 12c-.8-1.2-1.5-2.5-1.9-4h3.8c-.4 1.5-1.1 2.8-1.9 4zm2.3-6H9.7a14.7 14.7 0 0 1 0-4h4.6a14.7 14.7 0 0 1 0 4zm.3 5.6c.6-1.1 1.1-2.3 1.4-3.6h2.9a8 8 0 0 1-4.3 3.6zm1.7-5.6a16.5 16.5 0 0 0 0-4h3.4a8 8 0 0 1 0 4h-3.4z"/></svg>
      </div>
      <ul class="contact__list">
        <li>004791234567</li>
        <li>korbalt.llc@mailbox.com</li>
        <li>www.korbalt.llc</li>
      </ul>
    </div>
  </section>

</main>
</body>
</html>
```